Corporate Brochure for boutique Australian financial planning firm

We are looking for a face-lift with our company corporate brochure. This brochure will be used to show who we are, what we do, etc. to new potential clients. It will form part of an introductory pack that we give to clients after an initial free consultation.

The target market is generally people over 45 years old, including couples and singles, seeking financial advice.

We have a new logo and would like to implement elements of the logo design into the brochure.

There is a bit of text on the brochure so perhaps 3 double sided A4 pages (6 pages in total) with a trifold might work best.

The colours in our logo are black and red. We are looking to use these colours and maybe also white and grey?

We are after a contemporary, clean, minimalist design using elements/shapes/forms of our logo design in there so it's not generic and speaks out as 'ours'. It needs to be professional but not traditional looking if that makes sense.

This brochure will be used in emails but mostly in print form so it needs to be designed print-ready but in a readable format that we can also send via email.

Here are some things that might help, including attachments:
Our company website: http://corvenwealth.com.au

NOTE
In the New Corporate Brochure Content attachment, the pages have been laid out with printing in mind. So pages 1-3 in the PDF are for the "inside" of the brochure, pages 4-6 are for the "outside" of the brochure. So the front page would be page 6 from the PDF, and the back page would be page 4.

Target Market(s)

Australian couples and singles generally over 45 years old who are seeking financial advice

Industry/Entity Type

Financial Planning

Font styles to use
Sans Serif

Requirements
Must have
• Print-ready for 3 double sided A4 pages (6 pages in total with a trifold)
• Our company logo + other graphics (all in 'Must Use' graphics folder)
• The red colour that's in our logo.
• White background - clean aesthetic.
• Our financial planning process graphic can be kept as is or re-designed to suit space.
Should not have
• Title 'Corporate Brochure'

```html
<!DOCTYPE html>
<html lang="en">
<head>
<meta charset="utf-8">
<title>Corven Wealth – Brochure Inside Spread</title>
<link rel="stylesheet" href="https://fonts.googleapis.com/css2?family=Roboto:wght@300;400;500;700;900&display=swap">
<style>
:root{
  --red:#e8513f;
  --black:#161616;
  --ink:#333;
  --grey:#8a8a8a;
  --grey-light:#d8d8d8;
  --paper:#ffffff;
  --bg:#e6e6e2;
  --photo-a:#5f6b7c;
  --photo-b:#c9ced6;
}
*{box-sizing:border-box;margin:0;padding:0}
html,body{width:832px;height:1200px;overflow:hidden}
body{background:var(--bg);font-family:'Roboto',sans-serif;color:var(--ink);position:relative}
.spread{position:absolute;left:16px;top:40px;width:800px;height:378px;display:flex;box-shadow:0 4px 14px rgba(0,0,0,.12)}
.panel{position:relative;width:266.67px;height:378px;background:var(--paper);overflow:hidden}
.panel + .panel{border-left:1px solid #eee}
.p{font-size:4.6px;line-height:1.45;color:var(--ink)}

/* Panel: meet your adviser */
.hero{position:absolute;left:0;top:0;width:100%;height:112px;background:linear-gradient(110deg,var(--photo-a),var(--photo-b))}
.hero-photo{position:absolute;right:10px;top:6px;width:90px;height:106px;background:linear-gradient(180deg,#b7bcc3,#eef0f2);border-radius:40px 40px 0 0}
.badges{position:absolute;left:34px;top:36px;display:flex;gap:12px}
.badge{width:26px;height:26px;border-radius:50%;background:#3b5fa8;border:2px solid #dfe4ee}
.badge.grey{background:#8f8f8f;border-color:#c8c8c8}
.hero-caption{position:absolute;left:22px;top:82px;width:110px;text-align:center;font-size:4.6px;color:#f2f2f2;line-height:1.4}
.band{position:absolute;left:0;top:112px;width:100%;height:40px;background:var(--red);display:flex;align-items:center;padding-left:76px}
.band h2{color:#fff;font-weight:700;font-size:12px;letter-spacing:.2px}
.about{position:absolute;left:14px;top:166px;width:240px}
.about h3{font-size:8px;font-weight:700;color:var(--black);margin-bottom:6px}
.about .p{margin-bottom:5px}
.press{position:absolute;left:22px;top:290px;display:grid;grid-template-columns:repeat(6,28px);gap:10px 9px}
.press span{height:9px;background:#c5ccd8;border-radius:1px}
.press span.dot{width:12px;height:12px;border-radius:50%;background:#2b2b2b;justify-self:center}
.press span.sq{width:12px;height:12px;background:#3e7fc1;justify-self:center}
.foot-red{position:absolute;left:0;bottom:0;width:100%;height:8px;background:var(--red)}

/* Panel: process */
.top-red{position:absolute;left:0;top:0;width:100%;height:12px;background:var(--red)}
.brand{position:absolute;left:18px;top:44px;display:flex;align-items:center;gap:5px}
.brand-mark{width:14px;height:14px;background:var(--black)}
.brand-name{font-size:9px;font-weight:400;color:var(--black);letter-spacing:.6px;line-height:1}
.intro{position:absolute;left:140px;top:40px;width:112px;font-size:3.8px;line-height:1.45;color:var(--grey)}
.intro b{color:var(--red);font-weight:500}
.proc-title{position:absolute;left:8px;top:96px;font-size:7px;color:var(--grey);font-weight:300}
.rule{position:absolute;left:0;top:106px;width:130px;height:1px;background:var(--grey-light)}
.process{position:absolute;left:0;top:80px}
.note{position:absolute;font-size:3.6px;line-height:1.45;color:var(--grey);text-align:center}
.note b{display:block;color:var(--red);font-weight:500}
.foot-black{position:absolute;left:18px;bottom:18px;width:22px;height:4px;background:var(--black)}
.bottom-band{position:absolute;left:0;bottom:0;width:100%;height:14px;background:var(--red)}

/* Panel: five questions */
.top-bar{position:absolute;right:20px;top:18px;width:22px;height:4px;background:var(--black)}
.five{position:absolute;left:10px;top:18px;font-size:76px;font-weight:900;color:var(--red);line-height:1}
.q-head{position:absolute;left:66px;top:30px;font-size:8px;font-weight:700;color:var(--black);line-height:1.25;letter-spacing:.2px}
.qa{position:absolute;left:12px;top:124px;width:240px}
.qa h4{font-size:4.8px;font-weight:700;color:var(--black);margin-top:9px;margin-bottom:2px}
.brand.end{left:auto;right:24px;top:auto;bottom:40px}

/* Team panel */
.team{position:absolute;left:196px;top:460px;width:440px;height:622px;background:var(--paper);box-shadow:0 4px 14px rgba(0,0,0,.12);overflow:hidden}
.portraits{display:flex;height:296px}
.portrait{flex:1;background:linear-gradient(180deg,#6f6f6f,#d2d2d2)}
.portrait + .portrait{border-left:4px solid #fff}
.names{display:flex;background:#e4e4e4;height:40px}
.names div{flex:1;text-align:center;padding-top:9px}
.names div + div{border-left:4px solid #fff}
.names strong{display:block;font-size:8px;font-weight:700;color:var(--black);letter-spacing:.3px;line-height:1.2}
.names em{display:block;font-style:normal;font-size:6px;color:var(--grey);margin-top:3px;line-height:1.2}
.bios{display:flex;height:286px}
.bio{flex:1;background:var(--red);padding:14px 10px;color:#fff;font-size:6.6px;line-height:1.5}
.bio + .bio{border-left:4px solid #fff}
.bio p + p{margin-top:9px}
</style>
</head>
<body>

<section class="spread">
  <!-- Meet your adviser -->
  <article class="panel panel-adviser">
    <div class="hero">
      <div class="badges"><span class="badge"></span><span class="badge grey"></span></div>
      <p class="hero-caption">Award-Winning Financial Planners<br>on Sydney's Northern Beaches</p>
      <div class="hero-photo" role="img" aria-label="Portrait photograph of adviser Marcus Hale"></div>
    </div>
    <div class="band"><h2>MEET YOUR ADVISER</h2></div>
    <div class="about">
      <h3>ABOUT</h3>
      <p class="p">Marcus Hale is the Director of Corven Wealth. He was awarded the prestigious 'Adviser of the Year' accolade in 2016 by the National Planners Council and was selected to join the Top Trusted Planners group as a result of outstanding feedback from his clients.</p>
      <p class="p">Marcus has a Bachelor of Mathematics. He is an accredited Super Fund Specialist, an Accredited Wealth Planner and one of Australia's only financial life planners.</p>
      <p class="p">A born and bred Northern Beaches boy, he has an active interest in many sports and with two young boys, you won't see him sitting idle. Between refereeing local football matches, teaching his boys to surf or lining up a birdie putt on the golf course, when he isn't working, Marcus is 'on the go'.</p>
      <p class="p">You may have seen him occasionally on the Metro Business channel program Money Matters Live, or quoted in publications including the National Business Daily and The Harbour City Gazette.</p>
    </div>
    <div class="press" aria-label="Media and membership listings">
      <span></span><span></span><span></span><span></span><span></span><span></span>
      <span class="dot"></span><span class="dot" style="background:#3e7fc1"></span><span class="sq"></span><span class="sq" style="background:#d33"></span><span class="sq" style="background:#333"></span><span class="sq" style="background:#222"></span>
      <span></span><span class="dot" style="background:#5a9bd4"></span><span class="sq" style="background:#555"></span><span class="sq" style="background:#b22"></span>
    </div>
    <div class="foot-red"></div>
  </article>

  <!-- Financial planning process -->
  <article class="panel panel-process">
    <div class="top-red"></div>
    <div class="brand"><span class="brand-mark"></span><span class="brand-name">CORVEN<br>WEALTH</span></div>
    <p class="intro"><b>No two people are exactly alike and similarly, no two financial plans are the same.</b><br>This is the time where we listen and learn about you, your values and your goals. We work with you to set out how to reach them.</p>
    <p class="proc-title">Our Financial Planning Process</p><div class="rule"></div>
    <svg class="process" width="267" height="200" viewBox="0 0 267 200">
      <circle cx="165" cy="102" r="66" fill="var(--red)"/>
      <circle cx="165" cy="102" r="32" fill="#fff"/>
      <rect x="158" y="82" width="14" height="40" rx="5" fill="#9a9a9a" role="img" aria-label="Person icon"/>
      <g fill="#fff" font-family="Roboto,sans-serif">
        <text x="182" y="52" font-size="3.6" font-weight="700">STEP ONE</text>
        <text x="182" y="59" font-size="6" font-weight="300">Discovery</text>
        <text x="202" y="110" font-size="3.6" font-weight="700">STEP TWO</text>
        <text x="202" y="117" font-size="6" font-weight="300">Interpret</text>
        <text x="140" y="140" font-size="3.6" font-weight="700">STEP THREE</text>
        <text x="140" y="147" font-size="6" font-weight="300">Mutual</text>
        <text x="140" y="154" font-size="6" font-weight="300">Commitment</text>
        <text x="104" y="88" font-size="3.6" font-weight="700">STEP FOUR</text>
        <text x="104" y="95" font-size="6" font-weight="300">90 Day</text>
        <text x="104" y="102" font-size="6" font-weight="300">Follow-Up</text>
      </g>
    </svg>
    <p class="note" style="left:8px;top:152px;width:66px"><b>Check that everything is in place</b>We meet to review the results you can expect and answer your questions. We also adjust your plan as needed.</p>
    <p class="note" style="left:8px;top:204px;width:66px"><b>Let's implement</b>We work with you to put your plan in place, step by step, so your future is secure.</p>
    <p class="note" style="left:200px;top:258px;width:56px"><b>Did we hear you correctly?</b>We want to be sure we understand you. So we present our findings and recommendations for the way ahead.</p>
    <p class="note" style="left:120px;top:290px;width:56px">Corven Wealth grows trusted, lasting relationships and we encourage you to take the time you need.</p>
    <div class="foot-black"></div>
    <div class="bottom-band"></div>
  </article>

  <!-- Five questions -->
  <article class="panel panel-questions">
    <div class="top-bar"></div>
    <div class="five">5</div>
    <p class="q-head">QUESTIONS<br>FOR<br>MARCUS</p>
    <div class="qa">
      <h4>WHAT DO YOU LOVE MOST ABOUT YOUR CAREER?</h4>
      <p class="p">Being able to help people live ideal and helping them understand how to use money.</p>
      <h4>WHAT IS YOUR EXPERIENCE AS A FINANCIAL ADVISER?</h4>
      <p class="p">I've always worked in a small, self-licensed business so my experience is more around solving clients most pressing financial challenges rather than meeting a sales target. Boutique firms tend to work differently to banks and large institutions.</p>
      <h4>WHAT TYPE OF CLIENTS DO YOU SPECIALISE IN?</h4>
      <p class="p">We look after 3 types of clients. Firstly, people who are suddenly single and face making financial decisions alone, often for the first time. Secondly, those who are winding down and don't want to spend their non-working years trying to teach themselves finance. And thirdly, couples with good incomes but no time to dedicate to their own financial wellbeing.</p>
      <h4>WHAT ARE THE THINGS YOU VALUE MOST IN LIFE?</h4>
      <p class="p">9 hours of sleep each night and weekends with family.</p>
      <h4>IF YOU WON THE LOTTERY TOMORROW, HOW WOULD YOU LIVE YOUR LIFE?</h4>
      <p class="p">I would continue to align my values with my action. And buy a better second-hand surfboard.</p>
    </div>
    <div class="brand end"><span class="brand-mark"></span><span class="brand-name">CORVEN<br>WEALTH</span></div>
  </article>
</section>

<!-- Team panel -->
<section class="team">
  <div class="portraits">
    <div class="portrait" role="img" aria-label="Black and white portrait of Marcus Hale"></div>
    <div class="portrait" role="img" aria-label="Black and white portrait of Karen Doyle"></div>
    <div class="portrait" role="img" aria-label="Black and white portrait of Amy Tran"></div>
  </div>
  <div class="names">
    <div><strong>MARCUS HALE</strong><em>principal adviser</em></div>
    <div><strong>KAREN DOYLE</strong><em>client manager</em></div>
    <div><strong>AMY TRAN</strong><em>office manager</em></div>
  </div>
  <div class="bios">
    <div class="bio">
      <p>Marcus is an Accredited Wealth Planner, has a Bachelor of Science (Maths) and is a Super Fund Specialist.</p>
      <p>He is the founder of Corven Wealth, a privately owned financial planning business based on the Northern Beaches and one of Australia's only Financial Life Planners.</p>
      <p>Having spent more than 30,000 hours in the financial services industry, Marcus's advice combines left-brain logic with right-brain understanding. He applies his expertise to each client, allowing them to spend their time doing the things that are important to them.</p>
    </div>
    <div class="bio">
      <p>Karen holds a Bachelor of Social Science and Diploma of Financial Services. When Marcus makes promises to clients, Karen is the person that makes sure each and every promise is fulfilled.</p>
      <p>Karen has worked in the financial services industry since the late 1980s in the UK and Australia.</p>
      <p>Her focus is on providing a reliable, efficient and welcome service for all clients so that they feel at ease with building a long-term relationship with Corven Wealth.</p>
    </div>
    <div class="bio">
      <p>Amy joined the Corven Wealth team in August 2016. Having a background in media and administration, Amy brings a fresh set of eyes to the business, having worked previously outside the financial services industry.</p>
      <p>Her focus is on enhancing our communications whilst attending to the day-to-day running of the business.</p>
    </div>
  </div>
</section>

</body>
</html>
```